Pest Control Company needs business card!

Hi there, we need a business card designed for our new Pest Control Company. Ideally this card will be simple, yet feel elegant and high end. We want to use the colours Orange, Black and White. Please see our attached logo for the exact colours.

Business card details:

Phone - 0461 275 804
Name - Gavin Holloway
Email - Info@steadfastverminguard.com.au

We would also like to include the following list with dot points:

SERVICES / INSPECTIONS

Termites, Wood Borers, Ants, Cockroaches, Spiders, Fleas, Mice, Rats, Bed Bugs, & More!

```html
<!DOCTYPE html>
<html lang="en">
<head>
<meta charset="utf-8">
<title>Steadfast Vermin Guard — Business Card</title>
<link href="https://fonts.googleapis.com/css2?family=Oswald:wght@700&family=Cabin:wght@400&family=Arimo:wght@400&display=swap" rel="stylesheet">
<style>
  :root {
    --page-bg: #ebecec;
    --orange: #ef7f1e;
    --orange-deep: #ec6a22;
    --orange-shade: #e8621f;
    --white: #ffffff;
    --ink: #2b2b2b;
  }
  * { margin: 0; padding: 0; box-sizing: border-box; }
  html, body { width: 1004px; height: 1200px; overflow: hidden; background: var(--page-bg); }
  .canvas { position: relative; width: 1004px; height: 1200px; }

  .card {
    position: absolute; left: 160px; width: 657px; height: 380px;
    border-radius: 17px; overflow: hidden;
    box-shadow: 9px 11px 10px rgba(0,0,0,.17);
  }
  .card--front { top: 127px; }
  .card--back { top: 671px; }
  .card__art { position: absolute; inset: 0; width: 100%; height: 100%; display: block; }

  .brand-name {
    position: absolute; color: var(--white);
    font-family: 'Oswald', sans-serif; font-weight: 700;
    text-transform: uppercase; line-height: 1; letter-spacing: .5px;
  }
  .card--front .brand-name { left: 0; right: 0; top: 44px; text-align: center; }
  .card--front .brand-name span { display: block; }
  .card--front .brand-name .brand-name__top { font-size: 60px; }
  .card--front .brand-name .brand-name__bottom { font-size: 46px; margin-top: 8px; }

  .services {
    position: absolute; left: 0; right: 0; top: 302px; text-align: center;
    font-family: 'Cabin', sans-serif; font-size: 19px; line-height: 24px; color: var(--ink);
  }
  .services ul { list-style: none; display: flex; flex-wrap: wrap; justify-content: center; padding: 0 70px; }
  .services li { display: inline-flex; align-items: center; margin: 0 4px; }
  .services li::before {
    content: ""; width: 6px; height: 6px; background: var(--orange); margin-right: 5px;
  }

  .holder-name {
    position: absolute; left: 0; right: 0; top: 44px; text-align: center;
    font-family: 'Oswald', sans-serif; font-weight: 700; font-size: 31px; line-height: 1;
    color: var(--white); text-transform: uppercase; letter-spacing: .3px;
  }
  .card--back .brand-name { left: 118px; top: 246px; }
  .card--back .brand-name span { display: block; }
  .card--back .brand-name .brand-name__top { font-size: 34px; }
  .card--back .brand-name .brand-name__bottom { font-size: 26px; margin-top: 4px; }

  .divider { position: absolute; left: 307px; top: 232px; width: 2px; height: 90px; background: var(--orange-shade); }

  .contact { position: absolute; left: 334px; font-family: 'Arimo', sans-serif; color: var(--ink); display: flex; align-items: center; }
  .contact--phone { top: 249px; font-size: 35px; line-height: 38px; }
  .contact--email { top: 296px; font-size: 15px; line-height: 18px; }
  .contact svg { flex: none; margin-right: 8px; }
</style>
</head>
<body>
<main class="canvas">

  <section class="card card--front">
    <svg class="card__art" viewBox="0 0 1150 665" preserveAspectRatio="none" aria-hidden="true">
      <rect width="1150" height="665" fill="var(--orange)"/>
      <path d="M0,348 C30,343 55,333 75,337 C160,328 270,463 345,465 C430,468 510,333 595,335 C700,336 800,488 920,485 C1040,483 1040,398 1150,385 L1150,665 L0,665Z" fill="var(--orange-shade)"/>
      <path d="M0,360 C30,355 55,345 75,349 C160,340 270,475 345,477 C430,480 510,345 595,347 C700,348 800,500 920,497 C1040,495 1040,410 1150,397 L1150,665 L0,665Z" fill="var(--white)"/>
    </svg>
    <h1 class="brand-name">
      <span class="brand-name__top">Steadfast</span>
      <span class="brand-name__bottom">Vermin Guard</span>
    </h1>
    <div class="services">
      <ul>
        <li>Termites</li><li>Wood Borers</li><li>Ants</li><li>Cockroaches</li><li>Spiders</li><li>Fleas</li>
        <li>Mice</li><li>Rats</li><li>Bed Bugs &amp; More!</li>
      </ul>
    </div>
  </section>

  <section class="card card--back">
    <svg class="card__art" viewBox="0 0 1150 665" preserveAspectRatio="none" aria-hidden="true">
      <rect width="1150" height="665" fill="var(--orange-deep)"/>
      <path d="M0,306 C30,310 50,318 75,316 C160,318 250,190 340,191 C430,192 510,330 595,326 C700,322 800,168 920,168 C1020,168 1040,260 1150,269 L1150,665 L0,665Z" fill="var(--orange)"/>
      <path d="M75,316 C160,318 250,190 340,191 C430,192 510,330 595,326 C700,322 800,168 920,168 C1000,168 1030,220 1070,245" fill="none" stroke="var(--white)" stroke-width="8"/>
    </svg>
    <h2 class="holder-name">Gavin Holloway</h2>
    <div class="brand-name">
      <span class="brand-name__top">Steadfast</span>
      <span class="brand-name__bottom">Vermin Guard</span>
    </div>
    <div class="divider"></div>
    <p class="contact contact--phone">
      <svg width="11" height="20" viewBox="0 0 11 20" aria-hidden="true"><rect x="1" y="1" width="9" height="18" rx="2" fill="none" stroke="var(--ink)" stroke-width="2"/><circle cx="5.5" cy="15.5" r="1" fill="var(--ink)"/></svg>
      0461 275 804
    </p>
    <p class="contact contact--email">
      <svg width="12" height="10" viewBox="0 0 12 10" aria-hidden="true"><rect x="0.75" y="0.75" width="10.5" height="8.5" fill="none" stroke="var(--ink)" stroke-width="1.5"/><path d="M1,1 L6,6 L11,1" fill="none" stroke="var(--ink)" stroke-width="1.5"/></svg>
      Info@steadfastverminguard.com.au
    </p>
  </section>

</main>
</body>
</html>
```